Garlic Farm for Farm Sales/Restaurant sales

Need a professional, but appealing to agriculture world. We are selling 27 kinds of Organic Garlic from a farm in Simla,CO. I have uploaded logo and business information-we are going to need a template, because I will need to use it for four separate people.
-We are trying to appeal to Farm to table restaurants
-As well as growers/farmers

Target Market(s)

Agriculture Sales/Restaurants-Organic

Industry/Entity Type

Agriculture

Contact Information for Business Card

Want it to look more unique then your average orbel mart card- I want it to look amazing

Font styles to use
Sans Serif

Colors
0455a3
ec1f27
fbed22
ffffff

Requirements
Must have
• Just be creative
Nice to have
• Colorful
Should not have
• plain

```html
<!DOCTYPE html>
<html lang="en">
<head>
<meta charset="utf-8">
<title>Ridgeline Garlic Co – Business Card</title>
<link href="https://fonts.googleapis.com/css2?family=Open+Sans:wght@400;700&display=swap" rel="stylesheet">
<style>
  :root{
    --brand-blue:#0455a3;
    --brand-red:#ec1f27;
    --brand-yellow:#fbed22;
    --brand-white:#ffffff;
    --ink-navy:#1d2a5c;
    --stage:#8a8a8a;
  }
  *{margin:0;padding:0;box-sizing:border-box}
  html,body{width:1200px;height:900px;overflow:hidden}
  body{
    background:var(--stage);
    font-family:"Open Sans",Arial,sans-serif;
    display:flex;align-items:center;justify-content:center;gap:60px;
  }
  .card{
    position:relative;width:540px;height:310px;border-radius:22px;overflow:hidden;
    background:var(--brand-blue);
  }
  .card-art{position:absolute;inset:0;width:100%;height:100%}
  .brand-name{
    position:absolute;font-weight:700;color:var(--ink-navy);
    letter-spacing:.5px;white-space:nowrap;
  }
  .card-front .brand-name{left:62px;top:38px;font-size:24px}
  .contact-list{
    position:absolute;left:28px;top:136px;list-style:none;
    color:var(--brand-white);font-size:14px;line-height:25px;
  }
  .contact-list li{display:flex;align-items:center;gap:9px}
  .contact-list svg{width:12px;height:12px;flex:none}
  .contact-list .address{padding-left:21px}
  .person{
    position:absolute;right:34px;top:150px;text-align:right;color:var(--brand-white);
  }
  .person-name{font-weight:700;font-size:22px;letter-spacing:1.5px;text-transform:uppercase}
  .person-title{font-size:16px;margin-top:2px}
  .accent-bar{position:absolute;right:0;top:206px;width:10px;height:30px;background:var(--brand-yellow)}
  .card-back .brand-name{
    left:0;right:0;top:50%;transform:translateY(-50%);text-align:center;font-size:34px;
  }
</style>
</head>
<body>

<section class="card card-front" aria-label="Business card front">
  <svg class="card-art" viewBox="0 0 540 310" preserveAspectRatio="none">
    <defs>
      <linearGradient id="emblemTone" x1="0" y1="0" x2="1" y2="1">
        <stop offset="0" stop-color="#c8202a"/>
        <stop offset="1" stop-color="#f6d21a"/>
      </linearGradient>
    </defs>
    <path class="wave-accent" d="M0,108 C90,92 170,92 270,118 C390,148 470,120 540,60 V92 C470,150 390,168 270,132 C170,104 90,104 0,118 Z" fill="var(--brand-yellow)"/>
    <path class="wave-white" d="M0,0 H540 V42 C470,112 390,138 270,112 C170,88 90,88 0,104 Z" fill="var(--brand-white)"/>
    <path d="M215,310 C260,250 380,222 540,232 V310 Z" fill="url(#emblemTone)" role="img" aria-label="Large brand emblem decoration in red and yellow"/>
  </svg>

  <span class="brand-name">Ridgeline Garlic Co</span>

  <ul class="contact-list">
    <li>
      <svg viewBox="0 0 12 12"><rect x="3" y="0.8" width="6" height="10.4" rx="1.2" fill="none" stroke="#fff" stroke-width="1.2"/></svg>
      719-555-0142
    </li>
    <li>
      <svg viewBox="0 0 12 12"><rect x="0.8" y="2.2" width="10.4" height="7.6" fill="none" stroke="#fff" stroke-width="1.2"/><path d="M1,2.6 6,6.8 11,2.6" fill="none" stroke="#fff" stroke-width="1.2"/></svg>
      Dana@RidgelineGarlic.com
    </li>
    <li>
      <svg viewBox="0 0 12 12"><circle cx="6" cy="6" r="5.2" fill="none" stroke="#fff" stroke-width="1.2"/><path d="M0.8,6 H11.2 M6,0.8 C3,4 3,8 6,11.2 M6,0.8 C9,4 9,8 6,11.2" fill="none" stroke="#fff" stroke-width="1"/></svg>
      RidgelineGarlic.com
    </li>
    <li class="address">P.O. Box 48 Alder Flats, CO 80912</li>
  </ul>

  <div class="person">
    <p class="person-name">Dana Wells</p>
    <p class="person-title">Ceo/Founder</p>
  </div>
  <span class="accent-bar"></span>
</section>

<section class="card card-back" aria-label="Business card back">
  <span class="brand-name">Ridgeline Garlic Co</span>
</section>

</body>
</html>
```